Business Card for Makeup Artist

I need a business card designed for my makeup and hair artistry business which is primarily events and weddings focused. The card needs to be sleek, simple, stylish and appealing to women. I would prefer a white background but open to suggestions also. I also love the marble background look. I have attached some example pics. It needs to be a double sided card with logo and/or design on one side and contact details in the centre of the card on the other side. NO LOGO ON BACK. Examples attached.

Target Market(s)

Females age 14-55

Industry/Entity Type

Business

Contact Information for Business Card

Nora Pelling
Principal Makeup Artist
P: 0412 903 251
E: nora@lumivamakeup.com.au
W: www.lumivamakeup.com.au

Requirements
Should not have
• No yellow, green, red or blue in the design.

```html
<!DOCTYPE html>
<html lang="en">
<head>
<meta charset="utf-8">
<title>Lumiva Makeup Artistry – Business Card</title>
<link rel="stylesheet" href="https://fonts.googleapis.com/css2?family=Josefin+Sans:wght@200;300;400&family=Open+Sans:wght@400;700&display=swap">
<style>
  :root {
    --ink: #231f20;
    --pink: #ec1e79;
    --paper: #ffffff;
    --backdrop: #8e8e8e;
    --marble-light: #f7f7f7;
    --marble-vein: #dcdcdc;
    --muted: #3a3a3a;
  }
  * { box-sizing: border-box; margin: 0; padding: 0; }
  html, body {
    width: 1200px; height: 960px; overflow: hidden;
    background: var(--backdrop);
  }
  .sheet {
    position: relative; width: 1200px; height: 960px;
    background: radial-gradient(ellipse at 50% 40%, #d9d9d9 0%, #a9a9a9 55%, var(--backdrop) 100%);
  }
  .brand-header {
    position: absolute; left: 70px; top: 60px;
    color: var(--ink);
  }
  .brand-header .brand-name {
    display: flex; align-items: center; gap: 22px;
    font-family: "Josefin Sans", sans-serif; font-weight: 400;
    font-size: 120px; line-height: 1; letter-spacing: 2px;
  }
  .brand-mark-dot {
    width: 26px; height: 26px; border-radius: 50%; background: var(--pink);
  }
  .brand-header .brand-tagline {
    margin-top: 18px; margin-left: 118px;
    font-family: "Josefin Sans", sans-serif; font-weight: 300;
    font-size: 40px; letter-spacing: 2px;
  }
  .card {
    position: absolute; top: 340px;
    width: 520px; height: 297px;
    background: var(--paper);
    box-shadow: 0 18px 36px rgba(0,0,0,.28), 0 2px 4px rgba(0,0,0,.2);
    overflow: hidden;
  }
  .card--front { left: 50px; }
  .card--back { left: 630px; }
  .marble-texture {
    position: absolute; inset: 0;
    background:
      linear-gradient(155deg, transparent 30%, rgba(180,180,180,.35) 33%, transparent 37%),
      linear-gradient(20deg, transparent 60%, rgba(190,190,190,.3) 63%, transparent 67%),
      linear-gradient(135deg, var(--marble-light) 0%, #ececec 45%, var(--marble-vein) 100%);
  }
  .front-lockup {
    position: absolute; inset: 0;
    display: flex; flex-direction: column; align-items: center; justify-content: center;
    color: var(--ink);
  }
  .front-lockup .brand-name {
    display: flex; align-items: center; gap: 12px;
    font-family: "Josefin Sans", sans-serif; font-weight: 400;
    font-size: 74px; line-height: 1; letter-spacing: 1px;
  }
  .front-lockup .brand-mark-dot { width: 16px; height: 16px; }
  .front-lockup .brand-tagline {
    margin-top: 10px;
    font-family: "Josefin Sans", sans-serif; font-weight: 300;
    font-size: 24px; letter-spacing: 2px;
  }
  .contact-block {
    position: absolute; left: 120px; top: 46px;
    color: var(--ink);
  }
  .person-name {
    font-family: "Josefin Sans", sans-serif; font-weight: 200;
    font-size: 40px; letter-spacing: 5px; line-height: 1;
    margin-left: 60px;
  }
  .person-role {
    font-family: "Open Sans", sans-serif; font-weight: 700;
    font-size: 13px; letter-spacing: 1px; color: var(--pink);
    margin: 8px 0 20px 60px; text-transform: uppercase;
  }
  .contact-list { list-style: none; }
  .contact-item {
    display: flex; align-items: center; gap: 14px;
    font-family: "Open Sans", sans-serif; font-size: 15px; color: var(--muted);
    height: 34px;
  }
  .contact-item svg { width: 28px; height: 28px; flex: none; }
  .contact-item .web-strong { font-weight: 700; color: var(--ink); }
</style>
</head>
<body>
<main class="sheet">
  <header class="brand-header">
    <div class="brand-name"><span class="brand-mark-dot"></span>Lumiva</div>
    <div class="brand-tagline">MAKEUP ARTISTRY</div>
  </header>

  <section class="card card--front" aria-label="Card front">
    <div class="marble-texture" role="img" aria-label="Soft white and grey marble texture background"></div>
    <div class="front-lockup">
      <div class="brand-name"><span class="brand-mark-dot"></span>Lumiva</div>
      <div class="brand-tagline">MAKEUP ARTISTRY</div>
    </div>
  </section>

  <section class="card card--back" aria-label="Card back">
    <div class="contact-block">
      <div class="person-name">Nora Pelling</div>
      <div class="person-role">Principal Makeup Artist</div>
      <ul class="contact-list">
        <li class="contact-item">
          <svg viewBox="0 0 24 24" fill="none" stroke="#231f20" stroke-width="1.4" aria-hidden="true">
            <path d="M6.5 3.5l3 3.5-2 2.2c1 2.3 3 4.3 5.3 5.3l2.2-2 3.5 3-1.8 2.8c-6.5-.5-12.5-6.5-13-13z"/>
          </svg>
          <span>0412 903 251</span>
        </li>
        <li class="contact-item">
          <svg viewBox="0 0 24 24" fill="none" stroke="#231f20" stroke-width="1.4" aria-hidden="true">
            <rect x="3" y="6" width="18" height="12"/><path d="M3 6l9 7 9-7"/>
          </svg>
          <span>nora@lumivamakeup.com.au</span>
        </li>
        <li class="contact-item">
          <svg viewBox="0 0 24 24" fill="none" stroke="#231f20" stroke-width="1.4" aria-hidden="true">
            <circle cx="12" cy="12" r="9"/><ellipse cx="12" cy="12" rx="4" ry="9"/>
            <path d="M3 12h18M4.5 7.5h15M4.5 16.5h15"/>
          </svg>
          <span>www.<span class="web-strong">lumivamakeup</span>.com.au</span>
        </li>
      </ul>
    </div>
  </section>
</main>
</body>
</html>
```